T&K VelaSwing Flyer Design Project

We need a brochure to advertise classes and workshops with a couple of Brazilian dance teachers in Sydney.

It should be double-sided and have text to be readable and printable in an A6 postcard size.

It should be eye-catching and the information needs to be clear and clean so that the information can be easily understood.
Updates

Hi there
We would like to go to print asap so the sooner we get designs the better- we will look favourably at designs that come in quickly!
Thanks

Target Market(s)

Dance students especially students of Zouk-Lambada - a sexy, fun, brazilian partner dance aged 25-45 years

Requirements
Must have
• The photograph of the couple of the front.

The VelaSwing logo in black and gold on the front and back.

The design should also refer to the logo in terms of colours and style. The design is not limited to the logo colours but should be complementary.

The following text on the front:

TOMAS BELCANTE AND RAQUEL DUVINHO IN SYDNEY
Zouk – Samba de Gafiera - Bolero

VelaSwing Sydney is proud to be hosting renowned stars of the international Zouk scene - TOMAS BELCANTE AND RAQUEL DUVINHO .

Tomas and Raquel are unforgettable performers and dancers as well as highly skilled teachers trained at the prestigious Heitor Quevasso School of Dance in Rio de Janeiro.

Tomas and Raquel will teach classes and bootcamps in Brazilian rhythms - Zouk, Samba de Gaffiera and Bolero as well as choreographies.

Get the best out of the Tomas and Raquel 2013 - purchase 1st Release Multi-Class Passes now. Future releases at higher prices.

1st Release Multi- Class Passes - Valid for any class between 1- June and 31 July 2013
16 Class Pass – $280
24 Class Pass - $410
* Zouk classes are subject to skill level. Please visit www.velaswing.com.au for more info.
** Some bootcamp classes are 2 hours long, these will be debited as 2 credits instead of one.

Performance Packages - $420
24 hours of instructor-led choreography training and a routine you can perform with your partner at any event in Australia.

The following text on the back:

Tomas has been personally trained for over 12 years by Heitor Quevasso in all Brazilian styles - Zouk Lambada, Bolero, Samba de Gafieira, Forro and Soltinho, as well as Tango and Waltz. He has his own dance company and academy in Rio de Janeiro that is an affiliate school of the Central Dance School of Heitor Quevasso.

Raquel commenced her dance career in classical ballet, jazz and contemporary and studied with many renowned teachers throughout Brazil and at the Kestrelova School of Dance in St Petersburg, Russia for two years. She instructs at Heitor Quevasso and dances with the Heitor Quevasso and Tomas Belcante Companies.

Programme

(insert here the timetable attached)
Should not have
• Other dancing photos or silhouettes
Any shadowed text
Text that is difficult to read

```html
<!DOCTYPE html>
<html lang="en">
<head>
<meta charset="utf-8">
<title>VelaSwing Sydney – Programme</title>
<link href="https://fonts.googleapis.com/css2?family=Patrick+Hand+SC&display=swap" rel="stylesheet">
<style>
  :root {
    --ink: #000000;
    --gold: #f7c500;
    --panel: #ffc60d;
    --bar: #3b2b06;
    --ring: #c99700;
  }
  html, body { margin: 0; padding: 0; overflow: hidden; }
  body { width: 851px; height: 1200px; background: var(--ink); }
  .flyer {
    position: relative; width: 851px; height: 1200px; overflow: hidden;
    background: var(--ink); color: var(--gold);
    font-family: "Patrick Hand SC", cursive;
  }
  .bio {
    position: absolute; left: 18px; width: 820px; margin: 0;
    font-size: 27px; line-height: 33px;
  }
  .bio--tomas { top: 12px; }
  .bio--raquel { top: 222px; }
  .programme-title {
    position: absolute; left: 14px; top: 592px; margin: 0;
    font-size: 30px; line-height: 34px; font-weight: normal;
    border-bottom: 2px solid var(--gold);
  }
  .timetable {
    position: absolute; left: 14px; top: 631px; width: 829px; height: 483px;
    background: var(--panel); color: var(--ink);
    font-size: 24px; line-height: 29px;
  }
  .row { position: absolute; left: 0; width: 100%; height: 29px; }
  .row span { position: absolute; top: 0; white-space: nowrap; }
  .day { left: 12px; }
  .time { left: 200px; }
  .class { left: 472px; }
  .row--head { top: 8px; font-size: 28px; }
  .row--head::after {
    content: ""; position: absolute; left: 8px; right: 8px; top: 36px;
    border-bottom: 2px solid var(--ink);
  }
  .footer-bar {
    position: absolute; left: 14px; top: 1120px; width: 695px; height: 51px;
    background: var(--bar);
  }
  .brand {
    position: absolute; left: 716px; top: 1128px; width: 130px; height: 64px;
    display: flex; align-items: center; gap: 6px;
    color: var(--gold); font-size: 20px;
  }
  .brand-dot {
    width: 18px; height: 18px; border-radius: 50%;
    border: 3px solid var(--ring); flex: none;
  }
</style>
</head>
<body>
<main class="flyer">
  <p class="bio bio--tomas">Tomas has been personally trained for over 12 years by Heitor Quevasso in all Brazilian styles - Zouk Lambada, Bolero, Samba de Gafieira, Forro and Soltinho, as well as Tango and Waltz. He has his own dance company and academy in Rio de Janeiro that is an affiliate school of the Central Dance School of Heitor Quevasso.</p>
  <p class="bio bio--raquel">Raquel commenced her dance career in classical ballet, jazz and contemporary and studied with many renowned teachers throughout Brazil and at the Kestrelova School of Dance in St Petersburg, Russia for two years. She instructs at Heitor Quevasso and dances with the Heitor Quevasso and Tomas Belcante Companies.</p>

  <h2 class="programme-title">Programme</h2>
  <section class="timetable">
    <div class="row row--head"><span class="day">Date</span><span class="time">Time</span><span class="class" style="left:560px">Class</span></div>

    <div class="row" style="top:58px"><span class="day">Monday</span><span class="time">8pm</span><span class="class">Zouk Mastery (Technique)</span></div>
    <div class="row" style="top:87px"><span class="day">Monday</span><span class="time">9pm - 10:30 pm</span><span class="class">Zouk Choreo Open Level</span></div>

    <div class="row" style="top:130px"><span class="day">Tuesday</span><span class="time">6 pm</span><span class="class">6 Week Bootcamp</span></div>
    <div class="row" style="top:159px"><span class="day">Tuesday</span><span class="time">7pm</span><span class="class">Bolero</span></div>
    <div class="row" style="top:188px"><span class="day">Tuesday</span><span class="time">8pm</span><span class="class">Gafi Intermediate</span></div>
    <div class="row" style="top:217px"><span class="day">Tuesday</span><span class="time">9pm - 10:30 pm</span><span class="class">Gafi Choreo</span></div>

    <div class="row" style="top:262px"><span class="day">Saturday</span><span class="time">1pm - 3pm</span><span class="class">2Week Intensive Bootcamp</span></div>
    <div class="row" style="top:291px"><span class="day">Saturday</span><span class="time">3pm - 4pm</span><span class="class">Zouk 3</span></div>
    <div class="row" style="top:320px"><span class="day">Saturday</span><span class="time">4:15pm - 5:15pm</span><span class="class">Zouk 4</span></div>
    <div class="row" style="top:349px"><span class="day">Saturday</span><span class="time">5:30 pm - 7pm</span><span class="class">Zouk Choreo Level 3+</span></div>

    <div class="row" style="top:396px"><span class="day">Sunday</span><span class="time">5pm - 6:30 pm</span><span class="class">Teacher Course</span></div>
    <div class="row" style="top:425px"><span class="day">Sunday</span><span class="time">7pm - 8pm</span><span class="class">Pre-Party Workshop</span></div>
    <div class="row" style="top:454px"><span class="day">Sunday</span><span class="time">8pm - 11pm</span><span class="class">Party</span></div>
  </section>

  <div class="footer-bar"></div>
  <div class="brand"><span class="brand-dot"></span><span>VelaSwing</span></div>
</main>
</body>
</html>
```